New E-Learning Website Design Wanted!

I am creating an E-learning website for those interested in getting certifications in the IT industry.
For example, courses related to VKT, Lomen, RJV certifications and national certifications in the IT industry in Japan will be offered.
You can think of sites such as Pindolia, Kestova, BrickSage, Minotell.
But I am targeting industries in Japan at the moment.
Also, I have uploaded screenshots of pages that I think are good.

The company is Velmont Data
I recently got my company logo designed so I attached pdf file to this project brief.
I would appreciate it if you can make the site match the color scheme of the logo.

Target Market(s)

I am targeting individuals as well as large IT companies in Japan

Industry/Entity Type

Education

Coding

Coded - Design and coding required

Number of Pages Required

4 page

Font styles to use
Sans Serif

Colors

Designer to choose colors to be used in the design.

Requirements
Must have
• One top page design
• One course page (https://tivokhub.example/courses/vkt-hosting-services)
• One learning page(where the learner can see the video)
• One blog page(https://info.tivokhub.example/resources?_ga=2.51827364.27461930.1629384756-830152947.1629384756)
Nice to have
• Pricing page

```html
<!DOCTYPE html>
<html lang="en">
<head>
<meta charset="UTF-8">
<title>Velmont Data – E-Learning</title>
<link href="https://fonts.googleapis.com/css2?family=Lato:wght@400;700;900&display=swap" rel="stylesheet">
<style>
:root{
  --navy:#0e2a47;
  --navy-deep:#0a1f37;
  --teal:#1a7f88;
  --teal-light:#2aa3a9;
  --teal-pale:#d7eef0;
  --ink:#1d2b3a;
  --muted:#5d6b78;
  --white:#ffffff;
  --line:#e3e8ee;
}
*{box-sizing:border-box;margin:0;padding:0}
html,body{width:1200px;height:2472px;overflow:hidden}
body{font-family:'Lato',sans-serif;color:var(--ink);background:var(--white);position:relative}
.section-title{font-size:34px;font-weight:900;color:var(--navy);text-align:center}

/* Hero */
.hero{position:absolute;left:0;top:0;width:1200px;height:470px;background:linear-gradient(180deg,var(--navy-deep),var(--navy));color:var(--white);overflow:hidden}
.hero-wave{position:absolute;left:0;bottom:0}
.nav{position:absolute;left:0;top:0;width:1200px;height:64px;display:flex;align-items:center;padding:0 60px}
.brand{display:flex;align-items:center;gap:10px;font-size:22px;font-weight:700;color:var(--white)}
.brand-dot{width:14px;height:14px;border-radius:50%;background:var(--teal-light)}
.nav-links{margin-left:auto;display:flex;align-items:center;gap:26px;font-size:13px}
.nav-btn{border:1px solid var(--white);border-radius:4px;padding:5px 14px}
.nav-signup{color:var(--teal-light);font-weight:700}
.hero-copy{position:absolute;left:140px;top:150px;width:470px}
.hero-copy h1{font-size:30px;line-height:1.25;font-weight:900}
.hero-copy p{font-size:12px;line-height:1.6;margin-top:14px;opacity:.8}
.btn{display:inline-block;font-size:12px;font-weight:700;padding:10px 22px;border-radius:4px}
.btn-teal{background:var(--teal);color:var(--white)}
.btn-outline{border:1px solid var(--teal);color:var(--teal)}
.hero-copy .btn{margin-top:22px}
.hero-art{position:absolute;left:640px;top:90px;width:380px;height:250px;border-radius:10px;background:linear-gradient(135deg,#2a6f8c,#17405f)}

/* Stats */
.stats{position:absolute;top:570px;left:0;width:1200px;display:flex;justify-content:center;gap:40px}
.stat-card{width:200px;height:230px;background:var(--white);border-radius:16px;box-shadow:0 8px 24px rgba(14,42,71,.14);text-align:center;padding-top:18px}
.stat-icon{width:120px;height:92px;margin:0 auto;border-radius:8px;background:linear-gradient(135deg,var(--teal-pale),#a9d5db)}
.stat-num{font-size:44px;font-weight:900;color:var(--navy);margin-top:18px}
.stat-label{font-size:12px;color:var(--muted);margin-top:4px}

/* Videos */
.videos-title{position:absolute;top:848px;width:1200px}
.videos-copy{position:absolute;left:260px;top:940px;width:230px}
.videos-copy h3{font-size:18px;font-weight:900;line-height:1.4;color:var(--navy)}
.videos-copy p{font-size:11px;line-height:1.6;color:var(--muted);margin-top:16px}
.videos-copy .btn{margin-top:22px}
.video-frame{position:absolute;left:520px;top:900px;width:540px;height:260px;border-radius:4px;background:linear-gradient(135deg,#8b7a6a,#4b4a4f);overflow:hidden}
.video-play{position:absolute;left:245px;top:105px}
.video-bar{position:absolute;left:0;bottom:0;width:540px;height:24px;background:rgba(0,0,0,.55)}

/* Pricing */
.pricing-title{position:absolute;top:1220px;width:1200px}
.pricing-sub{position:absolute;top:1270px;width:1200px;text-align:center;font-size:22px;font-weight:700;color:var(--navy)}
.pricing-band{position:absolute;left:0;top:1360px;width:1200px;height:230px;background:linear-gradient(90deg,var(--teal),var(--teal-light))}
.pricing-person{position:absolute;left:0;top:1330px;width:240px;height:280px;background:linear-gradient(180deg,#7dc2c6,#2e8d93)}
.plans{position:absolute;left:258px;top:1320px;display:flex;gap:22px}
.plan-card{width:212px;height:330px;background:var(--white);box-shadow:0 6px 20px rgba(14,42,71,.15)}
.plan-photo{height:140px;background:linear-gradient(135deg,#c9a987,#7e9aa8)}
.plan-body{padding:18px 20px}
.plan-body h4{font-size:15px;font-weight:900;color:var(--navy)}
.plan-body p{font-size:11px;line-height:1.55;color:var(--muted);margin-top:10px}
.plan-body .btn{margin-top:16px;padding:8px 18px;font-size:11px}

/* Testimonials */
.testi-title{position:absolute;top:1740px;width:1200px}
.testimonials{position:absolute;left:240px;top:1820px;display:flex;gap:20px}
.testi-card{width:350px;height:220px;background:var(--white);box-shadow:0 6px 22px rgba(14,42,71,.12);padding:20px 28px;text-align:center;position:relative}
.testi-quote{position:absolute;left:14px;top:10px;font-size:80px;font-weight:900;color:var(--line);line-height:1}
.testi-avatar{width:70px;height:70px;border-radius:50%;margin:0 auto;background:linear-gradient(135deg,#b89a86,#6b7d8f)}
.testi-card p{font-size:11px;line-height:1.6;color:var(--muted);margin-top:14px}
.testi-name{font-size:12px;font-weight:700;color:var(--navy);margin-top:10px}
.testi-role{font-size:10px;color:var(--muted)}

/* Footer */
.footer{position:absolute;left:0;top:2130px;width:1200px;height:342px;background:linear-gradient(180deg,var(--navy),var(--navy-deep));color:var(--white)}
.newsletter{position:absolute;left:240px;top:2080px;width:720px;height:110px;background:var(--teal);border-radius:4px;display:flex;align-items:center;padding:0 40px;color:var(--white);z-index:2}
.newsletter h3{font-size:16px;font-weight:700;line-height:1.2}
.newsletter h3 span{display:block;font-size:26px;font-weight:900}
.news-form{margin-left:auto;display:flex;width:320px;height:38px;background:var(--white);border-radius:3px}
.news-input{flex:1;font-size:11px;color:var(--muted);padding:12px 14px}
.news-send{width:44px;background:var(--navy);border-radius:0 3px 3px 0;display:flex;align-items:center;justify-content:center}
.footer-brand{position:absolute;left:120px;top:140px;display:flex;align-items:center;gap:12px;font-size:34px;font-weight:700}
.footer-brand .brand-dot{width:22px;height:22px}
.footer-col{position:absolute;top:100px;font-size:10px;line-height:1.9;opacity:.9}
.footer-col h5{font-size:13px;font-weight:700;margin-bottom:6px}
.col-about{left:460px;width:180px}
.col-links{left:670px;width:110px}
.col-contact{left:790px;width:200px}
.footer-rule{position:absolute;left:120px;top:290px;width:960px;height:1px;background:rgba(255,255,255,.15)}
.copyright{position:absolute;left:120px;top:306px;font-size:10px;opacity:.8}
.socials{position:absolute;right:120px;top:300px;display:flex;gap:8px}
.socials span{width:22px;height:22px;border-radius:50%;background:var(--white);opacity:.9}
</style>
</head>
<body>

<header class="hero">
  <nav class="nav">
    <div class="brand"><span class="brand-dot"></span>Velmont Data</div>
    <div class="nav-links">
      <span>Courses</span><span>Features</span><span>For Business</span><span>Pricing</span><span>About Us</span>
      <span class="nav-btn">Sign In</span><span class="nav-signup">Sign Up</span>
    </div>
  </nav>
  <div class="hero-copy">
    <h1>Provide best learning experience to become a Software Architect</h1>
    <p>Individuals and companies who want their employees to level up their skills in cloud and programming find the path to IT certification with courses built for Japan.</p>
    <span class="btn btn-teal">Browse Courses</span>
  </div>
  <div class="hero-art" role="img" aria-label="Illustration of a desktop computer with floating course windows"></div>
  <svg class="hero-wave" width="1200" height="150" viewBox="0 0 1200 150">
    <path d="M0 90 C260 20 480 130 760 70 C960 30 1090 60 1200 40 L1200 150 L0 150 Z" fill="#1a7f88" opacity=".45"/>
    <path d="M0 110 C300 50 520 150 800 95 C990 60 1100 90 1200 70 L1200 150 L0 150 Z" fill="#ffffff"/>
  </svg>
</header>

<section class="stats">
  <div class="stat-card">
    <div class="stat-icon" role="img" aria-label="Illustration of a learner at a laptop"></div>
    <div class="stat-num">250</div><div class="stat-label">Hours of Learning</div>
  </div>
  <div class="stat-card">
    <div class="stat-icon" role="img" aria-label="Illustration of a video course screen"></div>
    <div class="stat-num">543</div><div class="stat-label">Courses</div>
  </div>
  <div class="stat-card">
    <div class="stat-icon" role="img" aria-label="Illustration of quiz sheets and devices"></div>
    <div class="stat-num">115</div><div class="stat-label">Quizzes</div>
  </div>
</section>

<h2 class="section-title videos-title">Videos</h2>
<div class="videos-copy">
  <h3>Lorem Ipsum is simply dummy text of the printing and typesetting industry. Lorem Ipsum has been the industry's standard dummy text ever since the</h3>
  <p>Lorem Ipsum is simply dummy text of the printing and typesetting industry. Lorem Ipsum has been the industry's standard dummy text ever since.</p>
  <span class="btn btn-teal">See More Videos</span>
</div>
<div class="video-frame" role="img" aria-label="Video still of a student studying at a table">
  <svg class="video-play" width="50" height="50" viewBox="0 0 50 50"><circle cx="25" cy="25" r="25" fill="#ffffff"/><path d="M20 15 L36 25 L20 35 Z" fill="#0e2a47"/></svg>
  <div class="video-bar"></div>
</div>

<h2 class="section-title pricing-title">Pricing</h2>
<div class="pricing-sub">Will offer subscriptions as well as individual courses</div>
<div class="pricing-band"></div>
<div class="pricing-person" role="img" aria-label="Photo of a smiling student with a notebook"></div>
<div class="plans">
  <div class="plan-card">
    <div class="plan-photo" role="img" aria-label="Photo of a student working on a laptop"></div>
    <div class="plan-body"><h4>Programming Subscription</h4><p>Training courses for national certification are one time payment courses</p><span class="btn btn-outline">View Subscription Plan</span></div>
  </div>
  <div class="plan-card">
    <div class="plan-photo" role="img" aria-label="Photo of a student reading outdoors"></div>
    <div class="plan-body"><h4>Cloud Subscription</h4><p>Training courses for national certification are one time payment courses</p><span class="btn btn-outline">View Subscription Plan</span></div>
  </div>
  <div class="plan-card">
    <div class="plan-photo" role="img" aria-label="Photo of children learning together in class"></div>
    <div class="plan-body"><h4>All in One Subscription</h4><p>Training courses for national certification are one time payment courses</p><span class="btn btn-outline">View Subscription Plan</span></div>
  </div>
</div>

<h2 class="section-title testi-title">Testimonials</h2>
<div class="testimonials">
  <div class="testi-card">
    <span class="testi-quote">“</span>
    <div class="testi-avatar" role="img" aria-label="Portrait photo of a student"></div>
    <p>Lorem Ipsum is simply dummy text of the printing and typesetting industry. Lorem Ipsum has been the industry's standard dummy text ever since the 1500s, when an unknown printer took a galley of type.</p>
    <div class="testi-name">Ken Mori Sato</div><div class="testi-role">Cloud Engineer</div>
  </div>
  <div class="testi-card">
    <span class="testi-quote">“</span>
    <div class="testi-avatar" role="img" aria-label="Portrait photo of a student"></div>
    <p>Lorem Ipsum is simply dummy text of the printing and typesetting industry. Lorem Ipsum has been the industry's standard dummy text ever since the 1500s, when an unknown printer took a galley.</p>
    <div class="testi-name">Yumi Hara</div><div class="testi-role">Software Developer</div>
  </div>
</div>

<div class="newsletter">
  <h3>Subscribe to<span>Newsletters</span></h3>
  <div class="news-form">
    <span class="news-input">Email address</span>
    <span class="news-send"><svg width="16" height="16" viewBox="0 0 16 16"><path d="M2 8 H13 M9 4 L13 8 L9 12" stroke="#ffffff" stroke-width="2" fill="none"/></svg></span>
  </div>
</div>

<footer class="footer">
  <div class="footer-brand"><span class="brand-dot"></span>Velmont Data</div>
  <div class="footer-col col-about">
    <h5>About us</h5>
    Lorem Ipsum is simply dummy text of the printing and typesetting industry. Lorem Ipsum has been the industry's standard dummy text ever since the 1500s, when an unknown printer took a galley.
  </div>
  <div class="footer-col col-links">
    <h5>Quick Links</h5>
    Testimonials<br>Blog<br>Pricing<br>News<br>Sitemap<br>Terms
  </div>
  <div class="footer-col col-contact">
    <h5>Contact us</h5>
    Lorem Ipsum is simply dummy text of the printing and typesetting industry.<br>
    000-000-0000<br>info@velmontdata.example<br>velmontdata.example
  </div>
  <div class="footer-rule"></div>
  <div class="copyright">© 2020 Velmont Data All Right Reserved</div>
  <div class="socials"><span></span><span></span><span></span><span></span></div>
</footer>

</body>
</html>
```